Vantiro Hotels website as a homepage for several hotels in Indonesia & Malaysia

HOMEPAGE:
Vantiro Hotels & Resorts is a hotel management company that has 18 hotels under its roof. The network consist of hotels in Jakarta, Bandung, Bali, Lombok, and several other cities in Indonesia & malaysia.
I need a clean and interactive homepage that is easy for booking, displays my hotels' images, partners' promotions, coming soon hotels & open vacancies. all in scroll down format.
Responsive to mobile & tabs. Light and quick to open.
Design references: belmirastays.example
I provided some images of hotels & partners' logo for you to play with the design.
Although we have different hotel names without a specific brand, Vantiro is starting to build our brands by opening several hotels under our own brand : Kesi (budget hotel), Merun (3-star fresh and dynamic hotels) & Falvane (4-star hotels). We need these bradns to be highlighted in the homepage as well.
We will implement a booking engine as well in the website for online booking.
I need widgets for:
- Book now
- Check in / check out date
- Search (whereby guests will input city names and my hotels will appear according to the location).
Our hotels name / Hotel ID Code:
1. Hotel Solin by Merun, Jakarta / H0001
2. Kesi Tarupa, Jakarta / H0002
3. Coral by Merun, Bandung / H0003
4. Tex Sumbaran, Bandung / H0004
5. Tex Lindgard, Bandung / H0006
6. Tex Pejuang, Bandung / H0005
7. Zenith Merun Bali Kerobok, Bali / H0011
8. Halverin Plus Bali Kerobok, Bali / H0009
9. Tirta Malimbu Hotel, Lombok / H0012
10. Le Varenne Hotel & Convention, Medan / H0013
11. Sukaraya Hotel, Medan / H0014
12. The Harbourline Hotel & Suites, Melaka / H0015
13. Kesi Norbury Hotel, Jambi / H0016
14. Merun Pekanbaru, Pekanbaru / H0018
15. Skyport Transit Hotel, Jakarta /H0017
HOTELS' PAGE / MICROSITE (Vantiro.com/hotelxxx)
It's a page inside my website providing information about one particular hotel.
Just take one hotel to play around with the layout designs, if OK we can work further on other hotels pages.
Target Market(s)
business travelers, family vacationers, online booking savvy, people who are used to booking via online platform, individual travelers, weekenders.
Industry/Entity Type
Hotel
Coding
Coded - Design and coding required
Number of Pages Required
2 page
Font styles to use
Other font styles liked:
- nexa
Requirements
Must have
- Vantiro Hotels & Resorts logo
- Must be : Vantiro.com (domain is owned)
- Vantiro facebook page & instagram
- fb : Vantiro Hotels & Resorts
- ig : @vantirohotels
Nice to have
- a CRM platform to manage my MICROSITES where I can just add photos, hotel description, hotel contacts, "starts from" box for the room rate for any hotel coming in to network or required updates.
- Vice versa, where i can just remove a page of hotel no longer in the network.
Should not have
- heavy images

```html
<!DOCTYPE html>
<html lang="en">
<head>
<meta charset="utf-8">
<title>Vantiro Hotels &amp; Resorts</title>
<link rel="stylesheet" href="https://fonts.googleapis.com/css2?family=Roboto:wght@300;400;500;700&display=swap">
<style>
:root{
  --orange:#f26b21;
  --ink:#222;
  --text:#555;
  --muted:#999;
  --panel:#f7f7f7;
  --footer:#eeeeee;
  --brand-text:#444;
  --white:#fff;
}
*{box-sizing:border-box;margin:0;padding:0}
html,body{width:1200px;height:2362px;overflow:hidden;background:var(--white)}
body{position:relative;font-family:"Roboto",Arial,sans-serif;color:var(--ink)}
.abs{position:absolute}

/* header */
.site-header{position:absolute;left:0;top:0;width:1200px;height:94px;background:var(--white)}
.wordmark{position:absolute;font-family:"Roboto",Arial,sans-serif;font-weight:500;color:var(--brand-text);white-space:nowrap;line-height:1}
.site-header .wordmark{left:139px;top:36px;font-size:24px}
.main-nav{position:absolute;top:41px;left:491px;font-size:14px;color:#111}
.main-nav a{color:inherit;text-decoration:none;position:absolute;white-space:nowrap}

/* hero */
.hero{position:absolute;left:0;top:94px;width:1200px;height:481px;
  background:linear-gradient(90deg,#3a2c1a 0%,#7a4f1e 18%,#a66a22 40%,#c58a2e 60%,#d6a24a 80%,#b7873a 100%)}
.hero-kicker{position:absolute;top:161px;width:1200px;text-align:center;color:var(--white);font-size:26px;letter-spacing:.5px}
.hero-title{position:absolute;top:197px;width:1200px;text-align:center;color:var(--white);font-size:37px;letter-spacing:.5px}
.hero-arrow{position:absolute;top:194px}
.search-panel{position:absolute;left:139px;top:468px;width:921px;height:107px;background:rgba(242,107,33,.9)}
.search-title{position:absolute;left:36px;top:19px;color:var(--white);font-size:20px;display:flex;align-items:center;gap:8px}
.field{position:absolute;top:55px;height:33px;background:var(--white);font-size:12px;color:#aaa;display:flex;align-items:center;padding-left:10px}
.field svg{position:absolute;right:8px}
.book-btn{position:absolute;left:778px;top:55px;width:110px;height:33px;background:#1a1a1a;color:var(--white);font-size:12px;font-weight:500;display:flex;align-items:center;justify-content:center}

/* offers */
.section-title{position:absolute;width:1200px;text-align:center;font-size:22px;font-weight:400;color:var(--ink)}
.offer{position:absolute;top:671px;width:289px;height:197px;overflow:hidden;border:1px solid #e3e3e3}
.offer-head{position:absolute;left:24px;font-size:22px;color:var(--orange);letter-spacing:.5px}
.offer-sub{position:absolute;left:24px;font-size:17px;color:#222}
.pill{position:absolute;border-radius:16px;font-size:12px;display:flex;align-items:center;justify-content:center}

/* hotels */
.hotels{position:absolute;left:0;top:929px;width:1200px;height:344px;background:var(--panel);border-top:1px solid #e8e8e8}
.hotel-card{position:absolute;top:106px;width:217px}
.hotel-photo{width:217px;height:135px}
.hotel-name{margin-top:12px;text-align:center;color:var(--orange);font-size:15px;font-weight:500}
.hotel-note{margin-top:4px;text-align:center;color:var(--muted);font-size:10.5px}

/* why */
.why{position:absolute;left:0;top:1273px;width:1200px;height:389px;
  background:linear-gradient(180deg,#8fb6dd 0%,#b9d3ea 45%,#dfe9f1 65%,#8c9a7a 85%,#4c5a3c 100%)}
.why-box{position:absolute;left:135px;top:47px;width:333px;height:268px;background:rgba(255,255,255,.88)}
.why-title{position:absolute;top:33px;width:100%;text-align:center;font-size:24px;font-weight:400;color:#222}
.why-text{position:absolute;top:84px;left:15px;width:303px;text-align:center;font-size:12.5px;line-height:24px;color:#666}
.learn-btn{position:absolute;left:225px;top:294px;width:142px;height:38px;border-radius:19px;background:var(--orange);color:var(--white);font-size:13px;display:flex;align-items:center;justify-content:center}
.feature{position:absolute;top:81px;width:220px;text-align:center}
.feature-icon{width:104px;height:104px;border-radius:50%;background:var(--orange);border:3px solid rgba(255,255,255,.8);margin:0 auto;display:flex;align-items:center;justify-content:center}
.feature-name{margin-top:22px;font-size:17px;color:#222}
.feature-text{margin-top:8px;font-size:11.5px;line-height:19px;color:#777}

/* brands */
.brands-title{position:absolute;top:1697px;width:1200px;text-align:center;color:var(--orange);font-size:21px;font-weight:400}
.partner{position:absolute;width:200px;height:30px;text-align:center;font-size:26px;font-weight:700;color:#5a5a5a;line-height:30px}
.partner-square{position:absolute;left:239px;top:1756px;width:88px;height:88px;background:#8a8178;color:#fff;font-size:15px;display:flex;align-items:center;justify-content:center}

/* footer */
.site-footer{position:absolute;left:0;top:2003px;width:1200px;height:359px;background:var(--footer)}
.foot-col{position:absolute;top:52px}
.foot-col h4{font-size:15px;font-weight:400;color:#333;letter-spacing:.3px;margin-bottom:14px}
.foot-col li{list-style:none;font-size:12.5px;color:#555;line-height:27.6px}
.address{font-size:12px;color:#555;line-height:25px}
.contact-line{display:flex;align-items:center;gap:10px;font-size:19px;color:#444;margin-top:12px}
.contact-line.small{font-size:17px;margin-top:8px}
.foot-rule{position:absolute;left:161px;top:2284px;width:926px;height:1px;background:#cfcfcf}
.copyright{position:absolute;left:166px;top:2312px;font-size:12px;color:#666}
.site-footer-brand{left:783px;top:2309px;font-size:22px}
</style>
</head>
<body>

<header class="site-header">
  <div class="wordmark">Vantiro Hotels &amp; Resorts</div>
  <nav class="main-nav">
    <a href="#" style="left:0;top:-4px" aria-label="Home">
      <svg width="22" height="19" viewBox="0 0 22 19"><path d="M11 1 1 10h3v8h5v-5h4v5h5v-8h3z" fill="#f26b21"/></svg>
    </a>
    <a href="#" style="left:57px">ABOUT</a>
    <a href="#" style="left:134px">FIND YOUR HOTEL</a>
    <a href="#" style="left:292px">OFFERS</a>
    <a href="#" style="left:374px">WHY US?</a>
    <a href="#" style="left:465px">CONTACT</a>
  </nav>
</header>

<section class="hero">
  <div role="img" aria-label="Hotel bedroom with lamps, red armchair and curtains" style="position:absolute;inset:0"></div>
  <div class="hero-kicker">VIVAMUS PORTTITOR PURUS NISI</div>
  <div class="hero-title">CUM SOCIS NATOQUE PENATIBUS</div>
  <svg class="hero-arrow" style="left:132px" width="20" height="36" viewBox="0 0 20 36"><path d="M17 3 3 18l14 15" fill="none" stroke="#fff" stroke-width="3.5"/></svg>
  <svg class="hero-arrow" style="left:1052px" width="20" height="36" viewBox="0 0 20 36"><path d="M3 3l14 15L3 33" fill="none" stroke="#fff" stroke-width="3.5"/></svg>
</section>

<form class="search-panel">
  <div class="search-title">
    <svg width="20" height="20" viewBox="0 0 20 20"><circle cx="8" cy="8" r="6" fill="none" stroke="#fff" stroke-width="2.6"/><path d="M12.5 12.5 18 18" stroke="#fff" stroke-width="3"/></svg>
    FIND YOUR HOTEL NOW
  </div>
  <div class="field" style="left:36px;width:428px">
    <svg style="position:static;margin-right:6px" width="10" height="14" viewBox="0 0 10 14"><path d="M5 0a5 5 0 0 0-5 5c0 4 5 9 5 9s5-5 5-9a5 5 0 0 0-5-5z" fill="#bbb"/><circle cx="5" cy="5" r="2" fill="#fff"/></svg>
    Location, City Name
  </div>
  <div class="field" style="left:474px;width:145px">Check in
    <svg width="16" height="14" viewBox="0 0 16 14"><rect x="1" y="2" width="14" height="11" fill="none" stroke="#bbb" stroke-width="1.4"/><path d="M1 5h14M5 8h2M9 8h2M5 10.5h2M9 10.5h2" stroke="#bbb"/></svg>
  </div>
  <div class="field" style="left:625px;width:145px">Check out
    <svg width="16" height="14" viewBox="0 0 16 14"><rect x="1" y="2" width="14" height="11" fill="none" stroke="#bbb" stroke-width="1.4"/><path d="M1 5h14M5 8h2M9 8h2M5 10.5h2M9 10.5h2" stroke="#bbb"/></svg>
  </div>
  <div class="book-btn">BOOK NOW</div>
</form>

<svg class="abs" style="left:591px;top:593px" width="32" height="26" viewBox="0 0 32 26"><path d="M2 2h11l12 12-10 10L2 11z" fill="#f26b21"/><circle cx="7" cy="7" r="2" fill="#fff"/><path d="M16 2h3l12 12-10 10-1.5-1.5L28 14z" fill="#f26b21"/></svg>
<h2 class="section-title" style="top:626px">OUR SPECIAL OFFERS</h2>

<article class="offer" style="left:139px">
  <div role="img" aria-label="Couple relaxing in a pool" style="position:absolute;inset:0;background:linear-gradient(90deg,#e8f2f8 0%,#bcdcec 45%,#cfa88a 75%,#8fb7cc 100%)"></div>
  <div class="offer-head" style="top:28px">PREPARE FOR</div>
  <div class="offer-sub" style="top:56px">YOUR STAY</div>
  <div class="pill" style="left:24px;top:89px;width:96px;height:28px;background:var(--orange);color:#fff">Click here</div>
</article>

<article class="offer" style="left:455px">
  <div role="img" aria-label="Guest lounging beside a pool" style="position:absolute;inset:0;background:linear-gradient(135deg,#fff 0%,#fff 38%,#e9c9a4 50%,#7fb7d6 80%,#3c8fc0 100%)"></div>
  <div class="offer-head" style="top:20px">BEST DEALS</div>
  <div class="offer-sub" style="top:48px">OF THE DAY</div>
  <div class="pill" style="left:16px;top:78px;width:82px;height:24px;border:1.5px solid var(--orange);color:var(--orange);background:#fff;font-size:11px">View Offers</div>
</article>

<article class="offer" style="left:772px;border:none">
  <div role="img" aria-label="Hotel room under an orange overlay" style="position:absolute;inset:0;background:linear-gradient(135deg,#f58a3c 0%,#f26b21 50%,#e0561a 100%)"></div>
  <div style="position:absolute;top:50px;width:100%;text-align:center;color:#fff;font-size:21px;line-height:27px;letter-spacing:.5px">VIEW OUR<br>BEST PACKAGES</div>
  <div class="pill" style="left:77px;top:117px;width:122px;height:34px;border:1.5px solid #fff;color:#fff;font-size:14px;border-radius:17px">Click here</div>
</article>

<section class="hotels">
  <svg class="abs" style="left:592px;top:19px" width="17" height="26" viewBox="0 0 17 26"><path d="M8.5 0A8.5 8.5 0 0 0 0 8.5C0 15 8.5 26 8.5 26S17 15 17 8.5A8.5 8.5 0 0 0 8.5 0z" fill="#f26b21"/><circle cx="8.5" cy="8.5" r="3.3" fill="#fff"/></svg>
  <h2 class="section-title" style="top:57px">HOTELS &amp; DESTINATIONS</h2>
  <div class="hotel-card" style="left:139px">
    <div class="hotel-photo" role="img" aria-label="Twin bedroom with wall screen" style="background:linear-gradient(135deg,#5b4a3c,#a8998a 60%,#d8d2c8)"></div>
    <div class="hotel-name">Class aptent taciti</div>
    <div class="hotel-note">sociosqu ad litora torquent conubia</div>
  </div>
  <div class="hotel-card" style="left:373px">
    <div class="hotel-photo" role="img" aria-label="Dim bedroom with white bed" style="background:linear-gradient(135deg,#3a3632,#8a8279 55%,#cfc8bf)"></div>
    <div class="hotel-name">Fusce tellus Sed</div>
    <div class="hotel-note">sociosqu ad litora torquent conubia</div>
  </div>
  <div class="hotel-card" style="left:608px">
    <div class="hotel-photo" role="img" aria-label="Bright twin room with window" style="background:linear-gradient(135deg,#e6e6e0,#cfcac0 55%,#b8ad98)"></div>
    <div class="hotel-name">Donec dictum lectus</div>
    <div class="hotel-note">sociosqu ad litora torquent conubia</div>
  </div>
  <div class="hotel-card" style="left:844px">
    <div class="hotel-photo" role="img" aria-label="Suite with checkered floor" style="background:linear-gradient(135deg,#2e2e2e,#7a7168 55%,#c9c0b4)"></div>
    <div class="hotel-name">Proin nulla arcu</div>
    <div class="hotel-note">sociosqu ad litora torquent conubia</div>
  </div>
</section>

<section class="why">
  <div role="img" aria-label="Resort terrace with sky and mountain view" style="position:absolute;inset:0"></div>
  <div class="why-box">
    <h2 class="why-title">WHY CHOOSE US</h2>
    <p class="why-text">At cursus magna nisl nec elit Praesent<br>elementum elit at tellus<br>massa libero interdum nec interdum vel<br>blandit sed nulla In ullamcorper est eget<br>tempor cursus neque mi consectetuer mi a<br>ultricies massa est sed nisl Class</p>
  </div>
  <div class="learn-btn">LEARN MORE</div>

  <div class="feature" style="left:460px">
    <div class="feature-icon">
      <svg width="54" height="44" viewBox="0 0 54 44"><path d="M8 32a19 19 0 0 1 38 0z" fill="none" stroke="#fff" stroke-width="2.6"/><path d="M3 36h48" stroke="#fff" stroke-width="2.6"/><circle cx="27" cy="10" r="3" fill="none" stroke="#fff" stroke-width="2.4"/><path d="M16 24a12 12 0 0 1 8-7" fill="none" stroke="#fff" stroke-width="2"/></svg>
    </div>
    <div class="feature-name">Top Food</div>
    <div class="feature-text">tuer mi a ultricies massa<br>est sed nisl Class</div>
  </div>
  <div class="feature" style="left:666px">
    <div class="feature-icon">
      <svg width="54" height="40" viewBox="0 0 54 40"><path d="M4 6v30M50 24v12M4 24h46M4 30h46" stroke="#fff" stroke-width="3"/><rect x="10" y="14" width="10" height="8" rx="3" fill="#fff"/><path d="M22 22v-8h22a6 6 0 0 1 6 6v2z" fill="#fff"/></svg>
    </div>
    <div class="feature-name">Quality Service</div>
    <div class="feature-text">tuer mi a ultricies massa<br>est sed nisl Class</div>
  </div>
  <div class="feature" style="left:867px">
    <div class="feature-icon">
      <svg width="54" height="50" viewBox="0 0 54 50"><path d="M6 20a22 16 0 0 1 42-6z" fill="#fff"/><path d="M27 16 36 40" stroke="#fff" stroke-width="2.6"/><path d="M8 40l10-8h14l6 8z" fill="none" stroke="#fff" stroke-width="2.4"/><path d="M4 45h46" stroke="#fff" stroke-width="2.6"/></svg>
    </div>
    <div class="feature-name">Beach &amp; Relax</div>
    <div class="feature-text">tuer mi a ultricies massa<br>est sed nisl Class</div>
  </div>
</section>

<h2 class="brands-title">OUR BRANDS</h2>
<div class="partner-square">Falvane</div>
<div class="partner" style="left:369px;top:1785px">Kesi</div>
<div class="partner" style="left:565px;top:1785px">Aerolina</div>
<div class="partner" style="left:768px;top:1785px">Kanara Bank</div>
<div class="partner" style="left:188px;top:1892px">Bank Sentosa</div>
<div class="partner" style="left:385px;top:1892px">Merun</div>
<div class="partner" style="left:577px;top:1892px">Lunara Card</div>
<div class="partner" style="left:779px;top:1892px">Casa Verle</div>

<footer class="site-footer">
  <div class="foot-col" style="left:161px">
    <h4>QUICK LINKS</h4>
    <ul><li>About Us</li><li>Why We are</li><li>Our Team</li><li>Press &amp; News</li><li>Career</li></ul>
  </div>
  <div class="foot-col" style="left:343px">
    <h4>FIND YOUR HOTEL</h4>
    <ul><li>Lorem ipsum</li><li>Solor sit amet</li><li>consectetuer adipiscing</li><li>Elit Nam cursus</li><li>Nullam enim</li></ul>
  </div>
  <div class="foot-col" style="left:583px">
    <h4>RESOURCES</h4>
    <ul><li>Support</li><li>FAQ</li><li>Legal Service</li><li>Blogs</li><li>Clients &amp; Partners</li></ul>
  </div>
  <div class="foot-col" style="left:798px">
    <h4>CONTACT US</h4>
    <p class="address">418 Harbor Point Avenue Suite B20<br>Lakeview, OR 97031</p>
    <div class="contact-line">
      <svg width="26" height="26" viewBox="0 0 26 26"><path d="M6 2l5 5-3 3c1.5 3.5 4.5 6.5 8 8l3-3 5 5-3 4C12 24 2 14 2 5z" fill="none" stroke="#2b7bbf" stroke-width="1.8"/></svg>
      555 014 2288
    </div>
    <div class="contact-line small">
      <svg width="28" height="24" viewBox="0 0 28 24"><path d="M3 3h15v10H9l-4 4v-4H3z" fill="none" stroke="#2b7bbf" stroke-width="1.8"/><path d="M20 8h5v9h-2v3l-3-3h-7v-2" fill="none" stroke="#2b7bbf" stroke-width="1.8"/></svg>
      Send a message
    </div>
  </div>
</footer>
<div class="foot-rule"></div>
<div class="copyright">© 2016 Company Name &nbsp;All right reserved</div>
<div class="wordmark site-footer-brand">Vantiro Hotels &amp; Resorts</div>

</body>
</html>
```